Bright Harbor Guides Header

I'm looking for a website header for a company(BrightHarborGuides.com) that provides services around Agile transformations. Agile transformations are happening everywhere but it is dominant in the software industry where people are moving from developing software using a waterfall process to Agile practices (such as Scrum).
I have an initial idea that plays off of moving away from Waterfall. This would be a waterfall on the left/background and a person on a Stand Up Paddleboard, flatboat or boat steering the boat with the word AGILE sitting on top (as a big word). Although the boat is close to the waterfall, the boat is sitting in calm water. This represents leading teams and organizations out of the chaos of waterfall process and into the calm of Agile Practices.

for the logo, I'd like to see some options with the three letters intertwined.

Target Market(s)

IT consulting/software

Industry/Entity Type

Information Technology

Logo Text

It could be Bright Harbor Guides or BHG

Font styles to use
Serif
Sans Serif

```html
<!DOCTYPE html>
<html lang="en">
<head>
<meta charset="utf-8">
<title>Bright Harbor Guides Header</title>
<link href="https://fonts.googleapis.com/css2?family=Roboto:wght@400;500&display=swap" rel="stylesheet">
<style>
  :root {
    --mist-light: #eef0f6;
    --mist: #dde2ec;
    --spray: #6fd6cb;
    --turquoise: #22b0ab;
    --deep-water: #13707f;
    --nav-start: #3cc4b8;
    --nav-end: #1f9a9a;
    --headline: #3ccfc4;
    --brand: #12707a;
    --white: #ffffff;
  }
  html, body {
    margin: 0;
    padding: 0;
    overflow: hidden;
  }
  body {
    width: 1200px;
    height: 500px;
    font-family: "Roboto", Arial, sans-serif;
  }
  .site-header {
    position: relative;
    width: 1200px;
    height: 500px;
    overflow: hidden;
  }
  .hero-scene {
    position: absolute;
    inset: 0;
    background: linear-gradient(150deg,
      var(--mist-light) 0%,
      var(--mist) 44%,
      var(--spray) 53%,
      var(--turquoise) 60%,
      var(--deep-water) 86%);
  }
  .top-bar {
    position: absolute;
    left: 0;
    top: 0;
    width: 1200px;
    height: 47px;
    background: linear-gradient(90deg, var(--nav-start), var(--nav-end));
    opacity: 0.95;
  }
  .site-title {
    position: absolute;
    left: 53px;
    top: 10px;
    margin: 0;
    font-size: 21px;
    font-weight: 400;
    color: var(--white);
    line-height: 26px;
  }
  .main-nav a {
    position: absolute;
    top: 11px;
    font-size: 17px;
    line-height: 22px;
    color: var(--white);
    text-decoration: none;
  }
  .nav-services { left: 553px; }
  .nav-about { left: 695px; }
  .nav-images { left: 839px; }
  .nav-blog { left: 972px; }
  .nav-contact { left: 1083px; }
  .brand-mark {
    position: absolute;
    left: 64px;
    top: 72px;
    font-size: 114px;
    line-height: 1;
    font-weight: 500;
    color: var(--brand);
  }
  .hero-word {
    position: absolute;
    left: 338px;
    top: 132px;
    margin: 0;
    font-size: 173px;
    line-height: 1;
    font-weight: 400;
    letter-spacing: -0.01em;
    color: var(--headline);
  }
</style>
</head>
<body>
  <header class="site-header">
    <div class="hero-scene" role="img" aria-label="Misty waterfall on the left giving way to calm turquoise water on the right, with a woman standing on a paddleboard steering with a paddle"></div>

    <div class="top-bar">
      <p class="site-title">Bright Harbor Guides</p>
      <nav class="main-nav">
        <a class="nav-services" href="#">Services</a>
        <a class="nav-about" href="#">About us</a>
        <a class="nav-images" href="#">Images</a>
        <a class="nav-blog" href="#">Blog</a>
        <a class="nav-contact" href="#">Contact us</a>
      </nav>
    </div>

    <div class="brand-mark">BHG</div>
    <h1 class="hero-word">AGILE</h1>
  </header>
</body>
</html>
```